VFX Company Business Card Design Project

The Ember Vale is a decentralized Visual Effects Studio servicing the television and feature film industries.
Project Brief:
Take our logo that was previously designed on Pixel Harbor and make a double sided business card.
Requirements:
- Card MUST be double sided.
- Front of card MUST have the yellow part of our logo against the dark grey background.
- Back of card is completely up to the designer.
- Back of card must include the complete company logo.
Please follow these File Preparation guidelines:
http://printmoor.example/infopage?file=filetype_en&s=PrintMoor_new&lang=en
Industry/Entity Type
Business
Look and feel
Each slider illustrates characteristics of the customer's brand and the style your logo design should communicate.

```html
<!DOCTYPE html>
<html lang="en">
<head>
<meta charset="utf-8">
<title>The Ember Vale – Business Card</title>
<link rel="stylesheet" href="https://fonts.googleapis.com/css2?family=Mulish:wght@400;600&display=swap">
<style>
  :root {
    --backdrop: #2b2b2b;
    --card: #232323;
    --accent: #f7c531;
    --text-light: #e6e6e6;
    --shadow: rgba(0, 0, 0, 0.55);
  }
  * { box-sizing: border-box; margin: 0; padding: 0; }
  html, body {
    width: 1200px;
    height: 900px;
    overflow: hidden;
    background: var(--backdrop);
    font-family: "Mulish", sans-serif;
  }
  .card-spread {
    position: relative;
    width: 1200px;
    height: 900px;
  }
  .card {
    position: absolute;
    top: 293px;
    width: 515px;
    height: 314px;
    background: var(--card);
    box-shadow: 0 6px 18px var(--shadow);
  }
  .card--front { left: 72px; }
  .card--back { left: 614px; }

  /* Front */
  .front-brand {
    position: absolute;
    inset: 0;
    display: flex;
    flex-direction: column;
    align-items: center;
    justify-content: center;
    gap: 22px;
  }
  .brand-dot {
    width: 46px;
    height: 46px;
    border-radius: 50%;
    background: var(--accent);
  }
  .brand-name {
    color: var(--accent);
    font-weight: 600;
    font-size: 44px;
    letter-spacing: 0.5px;
    line-height: 1;
  }

  /* Back */
  .back-brand {
    position: absolute;
    left: 30px;
    top: 0;
    height: 100%;
    width: 210px;
    display: flex;
    align-items: center;
  }
  .back-brand .brand-name { font-size: 27px; }
  .divider {
    position: absolute;
    left: 257px;
    top: 56px;
    width: 2px;
    height: 208px;
    background: var(--accent);
  }
  .contact {
    position: absolute;
    left: 285px;
    top: 60px;
    color: var(--text-light);
    font-size: 13px;
    line-height: 16px;
  }
  .contact-name {
    color: var(--accent);
    font-size: 21px;
    font-weight: 400;
    line-height: 24px;
  }
  .contact-role {
    font-size: 14px;
    margin-bottom: 20px;
  }
  .contact-group { margin-bottom: 14px; }
  .contact-line {
    display: flex;
    align-items: flex-start;
    gap: 6px;
  }
  .contact-line .icon {
    width: 10px;
    height: 12px;
    flex: none;
    margin-top: 2px;
    fill: var(--accent);
  }
  .contact-line .indent { padding-left: 16px; }
</style>
</head>
<body>
<main class="card-spread">
  <section class="card card--front" aria-label="Card front">
    <div class="front-brand">
      <span class="brand-dot"></span>
      <span class="brand-name">The Ember Vale</span>
    </div>
  </section>

  <section class="card card--back" aria-label="Card back">
    <div class="back-brand">
      <span class="brand-name">The Ember Vale</span>
    </div>
    <div class="divider"></div>
    <div class="contact">
      <p class="contact-name">Marcus Aldren</p>
      <p class="contact-role">managing director</p>

      <div class="contact-group">
        <p class="contact-line">
          <svg class="icon" viewBox="0 0 10 12"><path d="M5 0a4 4 0 0 0-4 4c0 3 4 8 4 8s4-5 4-8a4 4 0 0 0-4-4zm0 5.6A1.6 1.6 0 1 1 5 2.4a1.6 1.6 0 0 1 0 3.2z"/></svg>
          <span>48 Lantern Row</span>
        </p>
        <p class="contact-line"><span class="indent">Millbrook, Oregon 97001</span></p>
      </div>

      <div class="contact-group">
        <p class="contact-line">
          <svg class="icon" viewBox="0 0 10 12"><path d="M2 0h6a1 1 0 0 1 1 1v10a1 1 0 0 1-1 1H2a1 1 0 0 1-1-1V1a1 1 0 0 1 1-1zm.5 1.5v7.5h5V1.5z"/></svg>
          <span>777 414 20 36</span>
        </p>
        <p class="contact-line">
          <svg class="icon" viewBox="0 0 10 12"><path d="M2.5 1h5v3h-5zM0 4.5h10v5H8V8H2v1.5H0zM2.5 9h5v2.5h-5z"/></svg>
          <span>777 414 20 37</span>
        </p>
      </div>

      <div class="contact-group">
        <p class="contact-line">
          <svg class="icon" viewBox="0 0 10 12"><path d="M0 3h10v6H0zM0.6 3.4 5 6.6l4.4-3.2" stroke="#232323" stroke-width="0.9"/></svg>
          <span>info@embervale.example</span>
        </p>
        <p class="contact-line">
          <svg class="icon" viewBox="0 0 10 12"><circle cx="5" cy="6" r="4.5"/><path d="M0.5 6h9M5 1.5v9M5 1.5c-2.4 2.4-2.4 6.6 0 9M5 1.5c2.4 2.4 2.4 6.6 0 9" stroke="#232323" stroke-width="0.7" fill="none"/></svg>
          <span>www.embervale.example</span>
        </p>
      </div>
    </div>
  </section>
</main>
</body>
</html>
```